Photography Price List DL flyer

In need of a double sided DL flyer to list prices for a photography business that is in the real estate industry. Will need to include logo and be themed to match. Price details and contact information are in the pdf attached.

Below are links to the logo and photos that can be used on the flyer.

Logo
https://www.filquarry.net/s/tmewqoral7bnzx/LogoFiles.zip?dl=0

Photos
https://www.filquarry.net/s/p3vhnkelo81rtw/Website_Images.zip?dl=0

Sorry people the photo examples I put the wrong link. I have fixed it in the brief but the proper link is: https://www.filquarry.net/s/p3vhnkelo81rtw/Website_Images.zip?dl=0

Also dimensions of a DL are 210mm x 99mm + 3m bleed. Thanks

Target Market(s)

Real estate agents

Industry/Entity Type

Business

Requirements
Must have
• Price lists and contact information

```html
<!DOCTYPE html>
<html lang="en">
<head>
<meta charset="utf-8">
<title>Brightside Photos – DL Price Flyer</title>
<link href="https://fonts.googleapis.com/css2?family=Jost:wght@500;600;700&family=Tinos:wght@700&family=Arimo:wght@400&display=swap" rel="stylesheet">
<style>
  :root{
    --canvas:#ececec;
    --teal-deep:#0d4d54;
    --teal-mid:#0c6d73;
    --teal-bright:#0f7c82;
    --lime:#a6d872;
    --coral:#ef5f68;
    --white:#ffffff;
  }
  *{margin:0;padding:0;box-sizing:border-box}
  html,body{width:1200px;height:900px;overflow:hidden;background:var(--canvas)}
  .canvas{position:relative;width:1200px;height:900px}
  .flyer{position:absolute;top:68px;width:342px;height:729px;overflow:hidden;box-shadow:0 2px 8px rgba(0,0,0,.18)}
  .flyer--front{left:221px}
  .flyer--back{left:636px}
  .flyer__art{position:absolute;inset:0;width:342px;height:729px;display:block}

  .brand{position:absolute;top:42px;left:0;width:342px;display:flex;align-items:center;justify-content:center;gap:12px}
  .brand__name{font-family:"Jost",sans-serif;font-weight:600;color:var(--coral);font-size:27px;line-height:1;letter-spacing:.5px;text-align:center}
  .brand__name span{display:block;font-size:12px;letter-spacing:7px;margin-top:3px}
  .brand__mark{width:50px;height:50px;border-radius:50%;background:var(--coral)}

  .contact{position:absolute;top:660px;left:0;width:342px;text-align:center;font-family:"Arimo",sans-serif;font-size:14.5px;line-height:18.5px;color:var(--white)}

  .prices-title{position:absolute;top:20px;left:0;width:342px;text-align:center;font-family:"Jost",sans-serif;font-weight:700;font-size:26px;color:var(--lime)}
  .service{position:absolute;left:111px;font-family:"Jost",sans-serif;font-weight:700;font-size:21px;color:var(--white);line-height:1}
  .service small{font-family:"Tinos",serif;font-size:13px;color:var(--lime);margin-left:4px}
  .rates{position:absolute;left:111px;font-family:"Tinos",serif;font-weight:700;font-size:14px;line-height:21px;color:var(--lime)}
</style>
</head>
<body>
<main class="canvas">

  <!-- Front side -->
  <section class="flyer flyer--front">
    <svg class="flyer__art" viewBox="0 0 342 729" xmlns="http://www.w3.org/2000/svg">
      <defs>
        <linearGradient id="frontExterior" x1="0" y1="0" x2="0" y2="1">
          <stop offset="0" stop-color="#3d82e0"/>
          <stop offset=".35" stop-color="#8fb4dc"/>
          <stop offset=".55" stop-color="#9a5a46"/>
          <stop offset=".8" stop-color="#5e9a3a"/>
          <stop offset="1" stop-color="#7a8a5a"/>
        </linearGradient>
        <linearGradient id="frontInterior" x1="0" y1="0" x2="1" y2="1">
          <stop offset="0" stop-color="#dfe6ea"/>
          <stop offset=".6" stop-color="#c9935a"/>
          <stop offset="1" stop-color="#b46a2e"/>
        </linearGradient>
      </defs>
      <rect width="342" height="137" fill="var(--teal-deep)"/>
      <g fill="#1f6d6e">
        <circle cx="22" cy="8" r="3.5"/><circle cx="44" cy="8" r="3.5"/><circle cx="66" cy="8" r="3.5"/><circle cx="88" cy="8" r="3.5"/><circle cx="110" cy="8" r="3.5"/><circle cx="132" cy="8" r="3.5"/><circle cx="154" cy="8" r="3.5"/><circle cx="176" cy="8" r="3.5"/><circle cx="198" cy="8" r="3.5"/><circle cx="220" cy="8" r="3.5"/><circle cx="242" cy="8" r="3.5"/><circle cx="264" cy="8" r="3.5"/><circle cx="286" cy="8" r="3.5"/><circle cx="308" cy="8" r="3.5"/><circle cx="330" cy="8" r="3.5"/>
        <circle cx="22" cy="124" r="3.5"/><circle cx="44" cy="124" r="3.5"/><circle cx="66" cy="124" r="3.5"/><circle cx="88" cy="124" r="3.5"/><circle cx="110" cy="124" r="3.5"/><circle cx="132" cy="124" r="3.5"/><circle cx="154" cy="124" r="3.5"/><circle cx="176" cy="124" r="3.5"/><circle cx="198" cy="124" r="3.5"/><circle cx="220" cy="124" r="3.5"/><circle cx="242" cy="124" r="3.5"/><circle cx="264" cy="124" r="3.5"/><circle cx="286" cy="124" r="3.5"/><circle cx="308" cy="124" r="3.5"/><circle cx="330" cy="124" r="3.5"/>
      </g>
      <rect y="137" width="342" height="513" fill="url(#frontExterior)" role="img" aria-label="Photo of a brick family home with a tiled roof and front lawn"/>
      <path d="M0 418 Q170 425 342 520 L342 650 L0 650 Z" fill="url(#frontInterior)" role="img" aria-label="Photo of a bright living room interior with a timber staircase"/>
      <path d="M0 415 Q170 422 342 517" fill="none" stroke="var(--lime)" stroke-width="6"/>
      <path d="M0 645 Q150 500 342 432" fill="none" stroke="var(--coral)" stroke-width="7"/>
      <!-- service icons -->
      <circle cx="191" cy="502" r="52" fill="var(--coral)" opacity=".55"/>
      <circle cx="191" cy="502" r="44" fill="var(--teal-deep)"/>
      <g fill="var(--lime)">
        <rect x="163" y="486" width="56" height="36" rx="5"/>
        <rect x="176" y="479" width="18" height="9" rx="2"/>
      </g>
      <circle cx="191" cy="504" r="12" fill="var(--teal-deep)"/>
      <circle cx="191" cy="504" r="8" fill="var(--lime)"/>
      <circle cx="287" cy="464" r="35" fill="var(--teal-deep)"/>
      <g fill="var(--lime)">
        <circle cx="278" cy="453" r="8"/><circle cx="296" cy="453" r="8"/>
        <rect x="268" y="462" width="30" height="20" rx="3"/>
        <path d="M299 466 L310 460 L310 484 L299 478 Z"/>
      </g>
      <circle cx="75" cy="585" r="55" fill="var(--teal-deep)"/>
      <path d="M75 549 L112 582 L102 582 L102 612 L48 612 L48 582 L38 582 Z" fill="var(--lime)"/>
      <rect x="94" y="553" width="8" height="18" fill="var(--lime)"/>
      <rect y="650" width="342" height="79" fill="var(--teal-deep)"/>
    </svg>
    <div class="brand">
      <div class="brand__name">BRIGHTSIDE<span>PHOTOS</span></div>
      <div class="brand__mark"></div>
    </div>
    <p class="contact">mobile: 0400 517 264<br>web: brightsidephotos.com.au<br>email: hello@brightsidephotos.com.au</p>
  </section>

  <!-- Back side -->
  <section class="flyer flyer--back">
    <svg class="flyer__art" viewBox="0 0 342 729" xmlns="http://www.w3.org/2000/svg">
      <defs>
        <linearGradient id="backInterior" x1="0" y1="0" x2="1" y2="1">
          <stop offset="0" stop-color="#2f5fa8"/>
          <stop offset=".5" stop-color="#e8e4dc"/>
          <stop offset="1" stop-color="#8a6a4a"/>
        </linearGradient>
        <linearGradient id="backExterior" x1="0" y1="0" x2="0" y2="1">
          <stop offset="0" stop-color="#3a5a98"/>
          <stop offset=".5" stop-color="#c0504a"/>
          <stop offset="1" stop-color="#3a3440"/>
        </linearGradient>
      </defs>
      <rect width="342" height="729" fill="var(--teal-bright)"/>
      <rect x="32" y="82" width="278" height="460" fill="var(--teal-mid)"/>
      <rect width="342" height="82" fill="var(--teal-deep)"/>
      <g fill="#1f7f7c">
        <circle cx="16" cy="69" r="3.5"/><circle cx="40" cy="69" r="3.5"/><circle cx="64" cy="69" r="3.5"/><circle cx="88" cy="69" r="3.5"/><circle cx="112" cy="69" r="3.5"/><circle cx="136" cy="69" r="3.5"/><circle cx="160" cy="69" r="3.5"/><circle cx="184" cy="69" r="3.5"/><circle cx="208" cy="69" r="3.5"/><circle cx="232" cy="69" r="3.5"/><circle cx="256" cy="69" r="3.5"/><circle cx="280" cy="69" r="3.5"/><circle cx="304" cy="69" r="3.5"/><circle cx="328" cy="69" r="3.5"/>
      </g>
      <path d="M0 533 Q110 530 200 565 L342 565 L342 729 L0 729 Z" fill="url(#backInterior)" role="img" aria-label="Photo of a white lounge room interior at dusk"/>
      <path d="M60 729 Q170 580 342 520 L342 729 Z" fill="url(#backExterior)" role="img" aria-label="Twilight photo of a lit weatherboard house with front stairs"/>
      <path d="M0 532 Q110 528 200 570" fill="none" stroke="var(--lime)" stroke-width="6"/>
      <path d="M58 729 Q170 578 342 518" fill="none" stroke="var(--coral)" stroke-width="7"/>
      <!-- icons -->
      <g fill="var(--teal-deep)">
        <circle cx="77" cy="154" r="23"/><circle cx="77" cy="286" r="23"/><circle cx="77" cy="362" r="23"/><circle cx="77" cy="425" r="23"/>
      </g>
      <g fill="var(--lime)">
        <rect x="63" y="147" width="28" height="18" rx="3"/><rect x="70" y="143" width="9" height="5" rx="1"/>
        <path d="M71 274 L74 282 L82 282 L76 287 L78 295 L71 290 L64 295 L66 287 L60 282 L68 282 Z"/>
        <path d="M86 284 L87.5 288 L91 288 L88 290 L89 294 L86 292 L83 294 L84 290 L81 288 L84.5 288 Z"/>
        <path d="M80 296 L81.2 299 L84 299 L82 300.5 L82.6 303.5 L80 302 L77.4 303.5 L78 300.5 L76 299 L78.8 299 Z"/>
        <circle cx="71" cy="417" r="5"/><circle cx="82" cy="417" r="5"/>
        <rect x="65" y="422" width="20" height="12" rx="2"/><path d="M86 425 L93 421 L93 435 L86 431 Z"/>
      </g>
      <circle cx="77" cy="158" r="6" fill="var(--teal-deep)"/>
      <g fill="none" stroke="var(--lime)" stroke-width="2.5">
        <rect x="66" y="351" width="22" height="22"/>
        <path d="M66 362 L74 362 M77 351 L77 358 M77 366 L77 373 M80 362 L88 362"/>
      </g>
    </svg>
    <h1 class="prices-title">Prices</h1>
    <div class="service" style="top:142px">Photography</div>
    <p class="rates" style="top:172px">10 images $149<br>12-15 images $179<br>20+images $229</p>
    <div class="service" style="top:275px">Twilight</div>
    <p class="rates" style="top:308px;left:113px;font-size:15px">Add $100 to image package</p>
    <div class="service" style="top:351px">Floorplans <small>- $49</small></div>
    <div class="service" style="top:414px">Video</div>
    <p class="rates" style="top:448px">30 seconds $150<br>60 seconds $200<br>2 minutes $300</p>
  </section>

</main>
</body>
</html>
```